Lumen Gathering 2019 Enemies of the End-Times Church Flyer

We want a church conference flyer designed. We are looking for a professional, yet catchy design that uses our brand colors and logo creatively while communicating key information of the event effectively. <br/>The flyer must include all of the following:<br/>Title: Lumen Gathering 2019<br/>Topic: The Enemies of The End-Times Church <br/>Subtitles: <br/> -How the antichrist raises an army by social behavior engineering. <br/>-How the architects of modern social constructs escaped the church's radar. <br/>-The Holy Spirit's end-times agenda:<br/> The Knock-Out Punch!<br/>Speaker: Prophet Marcus Obuya <br/>Dates/time: December 27, 28 & 29 at 6pm<br/>Location: Thistle Community Center <br/> 412 Farrow Lane <br/> Portland, ME 04219<br/>Contact info: phone: 207-583-1924 <br/>email: contact@vellorbrook.org <br/> www.toskin.org<br/>*The flyer must also include a picture of the speaker and our Toskin logo <br/>Thanks, we look forward to seeing what you come up with!

Colors

Designer to choose colors to be used in the design.

Requirements
Must have
• The flyer must include all of the following:
• Title: Lumen Gathering 2019
• Topic: The Enemies of The End-Times Church
• Subtitles:
• -How the antichrist raises an army by social behavior engineering.
• -How the architects of modern social constructs escaped the church's radar.
• -The Holy Spirit's end-times agenda:
• The Knock-Out Punch!
• Speaker: Prophet Marcus Obuya
• Dates/time: December 27, 28 & 29 at 6pm
• Location: Thistle Community Center
• 412 Farrow Lane
• Portland, ME 04219
• Contact info: phone: 207-583-1924
• email: contact@vellorbrook.org
• www.toskin.org
• *The flyer must also include a picture of the speaker and our Toskin logo
Should not have
• Pictures of crosses or church buildings

```html
<!DOCTYPE html>
<html lang="en">
<head>
<meta charset="utf-8">
<title>Lumen Gathering 2019 – Flyer</title>
<link rel="stylesheet" href="https://fonts.googleapis.com/css2?family=Libre+Baskerville:wght@400;700&family=PT+Sans:wght@400;700&display=swap">
<style>
  :root {
    --navy: #0d3f7c;
    --navy-deep: #10306a;
    --sky-mid: #2d5c9a;
    --cloud: #eef1f5;
    --cloud-shade: #c9d4e2;
    --orange: #d9732a;
    --white: #ffffff;
    --page: #d3d9e1;
  }
  * { margin: 0; padding: 0; box-sizing: border-box; }
  html, body {
    width: 1200px; height: 1200px; overflow: hidden;
    background: var(--page);
  }
  .flyer {
    position: absolute; left: 140px; top: 20px;
    width: 920px; height: 1160px; overflow: hidden;
    background: linear-gradient(180deg, var(--navy-deep) 0%, var(--sky-mid) 35%, var(--cloud-shade) 55%, var(--cloud) 75%, #dfe5ec 100%);
    font-family: "Libre Baskerville", Georgia, serif;
    color: var(--navy);
  }
  .sky-scene {
    position: absolute; left: 0; top: 0; width: 920px; height: 640px;
    background:
      radial-gradient(ellipse 420px 260px at 480px 300px, rgba(240,170,190,0.35), transparent 70%),
      linear-gradient(180deg, rgba(16,48,106,0) 0%, rgba(16,48,106,0) 70%, rgba(238,241,245,0.6) 100%);
  }
  .speaker-photo {
    position: absolute; left: 165px; top: 107px; width: 456px; height: 494px;
    border-radius: 40% 40% 6px 6px;
    background: linear-gradient(180deg, rgba(120,90,70,0.55) 0%, rgba(143,176,216,0.8) 35%, rgba(201,217,238,0.7) 80%, rgba(238,241,245,0) 100%);
  }
  .dove { position: absolute; border-radius: 50%; background: radial-gradient(ellipse, rgba(255,255,255,0.95), rgba(255,255,255,0) 72%); }
  .dove--left { left: 80px; top: 110px; width: 200px; height: 155px; }
  .dove--right { left: 692px; top: 215px; width: 200px; height: 155px; }

  .frame-line { position: absolute; background: var(--orange); }
  .frame-line--top { left: 155px; top: 58px; width: 610px; height: 3px; }
  .frame-line--bottom { left: 155px; top: 1116px; width: 610px; height: 3px; }
  .frame-line--left { left: 59px; top: 150px; width: 3px; height: 870px; }
  .frame-line--right { left: 852px; top: 150px; width: 3px; height: 870px; }
  .corner-ornament {
    position: absolute; width: 90px; height: 95px;
    background: rgba(217,115,42,0.22); border-radius: 8px;
  }
  .corner-ornament--tl { left: 50px; top: 45px; }
  .corner-ornament--tr { left: 780px; top: 45px; }
  .corner-ornament--bl { left: 50px; top: 1030px; }
  .corner-ornament--br { left: 780px; top: 1030px; }

  .brand { position: absolute; left: 560px; top: 140px; width: 230px; text-align: center; }
  .brand__name { font-size: 52px; line-height: 1; color: var(--white); letter-spacing: 1px; }

  .line { position: absolute; left: 0; right: 0; text-align: center; line-height: 1; white-space: nowrap; }
  .title { top: 600px; font-size: 51px; font-weight: 700; color: var(--navy); }
  .topic { top: 657px; font-size: 28px; font-weight: 400; color: var(--orange); }
  .points {
    position: absolute; left: 70px; top: 702px; list-style: none;
    font-size: 14.2px; line-height: 19.5px; color: var(--navy); text-transform: uppercase;
  }
  .rule { position: absolute; left: 148px; width: 616px; height: 2px; background: var(--navy); }
  .rule--top { top: 781px; }
  .rule--bottom { top: 829px; }
  .speaker { top: 789px; font-family: "PT Sans", Arial, sans-serif; font-size: 36px; font-weight: 400; color: var(--navy); }
  .speaker strong { font-weight: 700; }
  .dates { top: 856px; font-size: 45px; font-weight: 400; }
  .venue { font-family: "PT Sans", Arial, sans-serif; color: var(--navy); }
  .venue--name { top: 928px; font-size: 29px; }
  .venue--address { top: 958px; font-size: 27px; letter-spacing: 0.5px; }
  .contact { font-family: "PT Sans", Arial, sans-serif; font-weight: 700; color: var(--navy); display: flex; justify-content: center; align-items: center; gap: 10px; }
  .contact--phone { top: 1020px; font-size: 38px; }
  .contact--online { top: 1076px; font-size: 25px; gap: 36px; }
  .contact__item { display: inline-flex; align-items: center; gap: 7px; }
  .icon { fill: var(--navy); }
</style>
</head>
<body>
  <main class="flyer">
    <div class="sky-scene" role="img" aria-label="Blue sky with light rays and soft white clouds"></div>
    <div class="speaker-photo" role="img" aria-label="Photo of the speaker preaching with an outstretched hand"></div>
    <div class="dove dove--left" role="img" aria-label="White dove in flight"></div>
    <div class="dove dove--right" role="img" aria-label="White dove in flight"></div>

    <div class="frame-line frame-line--top"></div>
    <div class="frame-line frame-line--bottom"></div>
    <div class="frame-line frame-line--left"></div>
    <div class="frame-line frame-line--right"></div>
    <div class="corner-ornament corner-ornament--tl" role="img" aria-label="Orange scroll corner ornament"></div>
    <div class="corner-ornament corner-ornament--tr" role="img" aria-label="Orange scroll corner ornament"></div>
    <div class="corner-ornament corner-ornament--bl" role="img" aria-label="Orange scroll corner ornament"></div>
    <div class="corner-ornament corner-ornament--br" role="img" aria-label="Orange scroll corner ornament"></div>

    <div class="brand">
      <div class="brand__name">TOSKIN</div>
    </div>

    <h1 class="line title">LUMEN GATHERING 2019</h1>
    <h2 class="line topic">THE ENEMIES OF THE END-TIMES CHURCH</h2>
    <ul class="points">
      <li>-How the antichrist raises an army by social behavior engineering.</li>
      <li>-How the architects of modern social constructs escaped the church's radar.</li>
      <li>-The Holy Spirit's end-times agenda: The knock-out punch!</li>
    </ul>

    <div class="rule rule--top"></div>
    <p class="line speaker">SPEAKER: <strong>PROPHET MARCUS OBUYA</strong></p>
    <div class="rule rule--bottom"></div>

    <p class="line dates">DECEMBER 27, 28 &amp; 29 AT 6PM</p>

    <p class="line venue venue--name">THISTLE COMMUNITY CENTER</p>
    <p class="line venue venue--address">412 Farrow Lane , Portland, ME 04219</p>

    <p class="line contact contact--phone">
      <svg class="icon" width="34" height="34" viewBox="0 0 24 24" aria-hidden="true"><path d="M6.6 10.8a15.1 15.1 0 0 0 6.6 6.6l2.2-2.2a1 1 0 0 1 1-.25 11.4 11.4 0 0 0 3.6.57 1 1 0 0 1 1 1V20a1 1 0 0 1-1 1A17 17 0 0 1 3 4a1 1 0 0 1 1-1h3.5a1 1 0 0 1 1 1c0 1.25.2 2.45.57 3.57a1 1 0 0 1-.25 1z"/></svg>
      207-583-1924
    </p>
    <p class="line contact contact--online">
      <span class="contact__item">
        <svg width="30" height="22" viewBox="0 0 30 22" aria-hidden="true"><rect x="1" y="1" width="28" height="20" fill="none" stroke="#0d3f7c" stroke-width="2"/><path d="M1 1l14 11L29 1" fill="none" stroke="#0d3f7c" stroke-width="2"/></svg>
        contact@vellorbrook.org
      </span>
      <span class="contact__item">
        <svg width="28" height="28" viewBox="0 0 28 28" aria-hidden="true" fill="none" stroke="#0d3f7c" stroke-width="2"><circle cx="14" cy="14" r="12"/><ellipse cx="14" cy="14" rx="5" ry="12"/><path d="M2 14h24M4 8h20M4 20h20"/></svg>
        www.toskin.org
      </span>
    </p>
  </main>
</body>
</html>
```